Trinket Crate Guild - New Website Design

Create a professional website for charms of the month club; a subscription box business. the website URL will be www.TrinketCrateGuild.com
Please see ruffleparcel.com; fudgeguild.com and pupcrate.com for the concept I am after. The business has not been launched yet, I am currently in the pre-launch stage using a specialized landing page website, and so the time scale for developing my professional looking website is up to 1-2 weeks.
The webpage should have a fun feel and should match the style of the company logo at fudgeguild.com or pupcrate.com. The pages to include are 'Home', 'About us' and 'Get Started'
Thank you and good luck!

```html
<!DOCTYPE html>
<html lang="en">
<head>
<meta charset="utf-8">
<title>Trinket Crate Guild</title>
<link rel="stylesheet" href="https://fonts.googleapis.com/css2?family=Alegreya:wght@700&family=Exo+2:wght@500&family=Lobster&family=Noto+Serif:ital,wght@0,400;1,400;1,700&family=Poppins:wght@300;400;500&family=Roboto:wght@400;500&display=swap">
<style>
:root{
  --coral:#fd5b5e;
  --coral-soft:#fd7080;
  --footer:#fd4a4b;
  --ink:#222;
  --muted:#555;
  --light:#f8f8f8;
  --white:#fff;
  --line:#e6e6e6;
}
*{margin:0;padding:0;box-sizing:border-box}
html,body{width:1200px;height:2314px;overflow:hidden}
body{position:relative;background:var(--white);font-family:"Poppins",sans-serif;color:var(--ink)}
.abs{position:absolute}

/* header */
.site-header{top:0;left:0;width:1200px;height:46px;background:var(--white)}
.brand{left:99px;top:11px;font-family:"Poppins",sans-serif;font-weight:500;font-size:18px;color:var(--coral);display:flex;align-items:center;gap:8px}
.brand-mark{width:14px;height:14px;background:var(--coral)}
.main-nav a{position:absolute;top:16px;font-family:"Roboto",sans-serif;font-size:15px;color:#333;text-decoration:none}
.sign-in{left:995px;top:9px;width:106px;height:30px;background:var(--coral);color:var(--white);font-family:"Roboto",sans-serif;font-weight:500;font-size:14px;display:flex;align-items:center;justify-content:center}

/* hero */
.hero{top:46px;left:0;width:1200px;height:552px;background:linear-gradient(100deg,#f3a9b7 0%,#f19aac 45%,#ee8fa2 100%)}
.hero-title{right:100px;top:223px;text-align:right;font-family:"Alegreya",serif;font-weight:700;font-size:43px;line-height:68px;color:var(--white)}
.hero-cta{left:776px;top:387px;width:325px;height:62px;background:var(--coral);border-radius:5px;color:var(--white);font-family:"Exo 2",sans-serif;font-weight:500;font-size:23px;letter-spacing:1.5px;display:flex;align-items:center;justify-content:center}

/* welcome */
.welcome-title{top:630px;left:0;width:1200px;text-align:center;font-family:"Noto Serif",serif;font-style:italic;font-size:27px}
.welcome-text{top:689px;left:190px;width:820px;text-align:center;font-size:10.5px;line-height:21px;color:var(--muted)}

/* feature */
.feature-heading{left:99px;top:832px;width:276px;text-align:right;font-family:"Noto Serif",serif;font-style:italic;font-size:20px;line-height:37px}
.feature-text{left:99px;top:922px;width:276px;text-align:right;font-size:10.5px;line-height:25.5px;color:var(--muted)}
.read-more{left:259px;top:1097px;width:113px;height:34px;border:1px solid #555;font-family:"Roboto",sans-serif;font-size:13px;display:flex;align-items:center;justify-content:center}
.feature-photo{left:399px;top:786px;width:371px;height:383px;background:radial-gradient(circle at 50% 55%,#6b5a56 0%,#8e7c6c 40%,#bfb3a0 100%)}
.feature-panel{left:770px;top:786px;width:330px;height:383px;background:var(--coral-soft);color:var(--white);text-align:center;font-family:"Noto Serif",serif;font-style:italic}
.panel-kicker{margin-top:62px;font-size:22px;line-height:40px}
.panel-headline{margin-top:22px;font-weight:700;font-size:31px;line-height:58px}

/* products */
.products{top:1228px;left:0;width:1200px;height:447px;background:var(--light)}
.section-title{font-family:"Noto Serif",serif;font-size:26px}
.products-title{left:99px;top:1272px}
.slider-dots{left:1033px;top:1284px;display:flex;gap:4px}
.slider-dots span{width:12px;height:12px;border-radius:50%;background:#777}
.slider-dots span:first-child{background:#bbb}
.product-img{top:1337px;width:319px;height:215px}
.product-text{top:1568px;width:319px;text-align:center;font-size:10.5px;line-height:23px;color:var(--muted)}

/* plans */
.plans-title{top:1716px;left:0;width:1200px;text-align:center;font-style:italic}
.plan{top:1784px;width:278px;height:392px;background:var(--white);border:1px solid var(--line)}
.plan.featured{box-shadow:0 8px 18px rgba(0,0,0,.22);border-color:transparent}
.plan-head{height:114px;color:var(--white);text-align:center}
.plan-name{padding-top:14px;font-family:"Lobster",cursive;font-size:36px;line-height:44px}
.plan-price{font-family:"Roboto",sans-serif;font-size:26px;line-height:32px}
.plan-features{list-style:none;text-align:center;margin-top:26px;font-size:11.5px;color:#444}
.plan-features li{height:42px}
.plan-buy{position:absolute;left:62px;top:326px;width:155px;height:33px}
.plan-buy svg{position:absolute;inset:0}
.plan-buy span{position:relative;display:flex;height:100%;align-items:center;justify-content:center;font-weight:500;font-size:13px;color:var(--white);letter-spacing:.5px}

/* footer */
.site-footer{top:2222px;left:0;width:1200px;height:92px;background:var(--footer);color:var(--white);text-align:center}
.footer-nav{margin-top:21px;font-size:14px}
.footer-nav a{color:var(--white);text-decoration:none;margin:0 12px}
.copyright{margin-top:12px;font-size:10.5px}
</style>
</head>
<body>

<header class="abs site-header">
  <div class="abs brand"><span class="brand-mark"></span>Trinket Crate Guild</div>
  <nav class="main-nav">
    <a style="left:716px">Home</a>
    <a style="left:809px">Blog</a>
    <a style="left:890px">Contact Us</a>
  </nav>
  <div class="abs sign-in">SIGN IN</div>
</header>

<section class="abs hero" role="img" aria-label="Photo of a smiling woman holding a pink gift box with balloons against a pink wall"></section>
<h1 class="abs hero-title">All Your Beautiful Things Comes<br>In A Single Box</h1>
<div class="abs hero-cta">Book Us Today</div>

<h2 class="abs welcome-title">Welcome To Trinket Crate Guild</h2>
<p class="abs welcome-text">Lorem Ipsum is simply dummy text of the printing and typesetting industry. Lorem Ipsum has been the industry's standard dummy text ever since the 1500s,<br>Lorem Ipsum is simply dummy text of the printing and typesetting industry. Lorem Ipsum has been the industry's standard dummy text ever since the 1500s,<br>Lorem Ipsum has been the industry's standard dummy text ever since the 1500s.</p>

<h3 class="abs feature-heading">Neque porro quisquam est<br>qui dolorem ipsum</h3>
<p class="abs feature-text">Lorem Ipsum is simply dummy text of the printing and typesetting industry. Lorem Ipsum has been the industry's standard dummy text ever since the 1500s, when an unknown printer took a galley of type and scrambled it to make a type specimen book. It has survived not only five centuries</p>
<div class="abs read-more">READ MORE</div>
<div class="abs feature-photo" role="img" aria-label="Photo of a woman opening a small red gift box in front of a festive tree with lights"></div>
<div class="abs feature-panel">
  <p class="panel-kicker">Neque porro quisquam<br>est qui dolorem</p>
  <p class="panel-headline">Suprise Your Gift<br>To Your<br>Loved Ones</p>
</div>

<section class="abs products"></section>
<h2 class="abs section-title products-title">Check Out Our Products</h2>
<div class="abs slider-dots"><span></span><span></span><span></span><span></span></div>
<div class="abs product-img" style="left:99px;background:linear-gradient(135deg,#e0142a,#c90f22)" role="img" aria-label="Photo of a white gift box with red ribbon and a bracelet on a red background"></div>
<div class="abs product-img" style="left:441px;background:linear-gradient(135deg,#6a4a33,#a9774e 55%,#8fb2d6)" role="img" aria-label="Photo of a perfume bottle beside a blue gift box on a wooden table"></div>
<div class="abs product-img" style="left:782px;background:linear-gradient(135deg,#9c9c9c,#b1a79e)" role="img" aria-label="Photo of a red-haired woman holding a small kraft gift box"></div>
<p class="abs product-text" style="left:99px">Lorem Ipsum is simply dummy text of the printing and typesetting industryLorem Ipsum is simply dummy text of the printing and typesetting industry</p>
<p class="abs product-text" style="left:441px">Lorem Ipsum is simply dummy text of the printing and typesetting industryLorem Ipsum is simply dummy text of the printing and typesetting industry</p>
<p class="abs product-text" style="left:782px">Lorem Ipsum is simply dummy text of the printing and typesetting industryLorem Ipsum is simply dummy text of the printing and typesetting industry</p>

<h2 class="abs section-title plans-title">Get Our Subscription Plans</h2>

<article class="abs plan" style="left:140px">
  <div class="plan-head" style="background:linear-gradient(135deg,#3a3a3a,#7a7470)" role="img" aria-label="Dark photo of a gift box with flowers">
    <div class="plan-name">Silver</div><div class="plan-price">$ 23.00</div>
  </div>
  <ul class="plan-features"><li>Neque porro quisquam est</li><li>Neque porro quisquam est</li><li>Neque porro quisquam est</li><li>Neque porro quisquam est</li></ul>
  <div class="plan-buy"><svg viewBox="0 0 155 33" width="155" height="33"><polygon points="0,0 155,0 148,33 7,33" fill="#fd5b5e"/></svg><span>BUY NOW</span></div>
</article>

<article class="abs plan featured" style="left:469px">
  <div class="plan-head" style="background:linear-gradient(135deg,#8a7f7a,#b5a9a2)" role="img" aria-label="Soft photo of a woman with a gift in a bright room">
    <div class="plan-name">Gold</div><div class="plan-price">$ 34.00</div>
  </div>
  <ul class="plan-features"><li>Neque porro quisquam est</li><li>Neque porro quisquam est</li><li>Neque porro quisquam est</li><li>Neque porro quisquam est</li></ul>
  <div class="plan-buy"><svg viewBox="0 0 155 33" width="155" height="33"><polygon points="0,0 155,0 148,33 7,33" fill="#fd5b5e"/></svg><span>BUY NOW</span></div>
</article>

<article class="abs plan" style="left:796px">
  <div class="plan-head" style="background:linear-gradient(135deg,#4a3530,#8a6e64)" role="img" aria-label="Photo of hands holding a gift box">
    <div class="plan-name">Platinum</div><div class="plan-price">$ 54.00</div>
  </div>
  <ul class="plan-features"><li>Neque porro quisquam est</li><li>Neque porro quisquam est</li><li>Neque porro quisquam est</li><li>Neque porro quisquam est</li></ul>
  <div class="plan-buy"><svg viewBox="0 0 155 33" width="155" height="33"><polygon points="0,0 155,0 148,33 7,33" fill="#fd5b5e"/></svg><span>BUY NOW</span></div>
</article>

<footer class="abs site-footer">
  <nav class="footer-nav"><a>Home</a><a>About us</a><a>Get started</a></nav>
  <p class="copyright">Copyright © 2017 Trinket Crate Guild. All Rights Reserved</p>
</footer>

</body>
</html>
```